KTR Football Academy Flyer

Flyer for a full page of a yearbook ( dimensions below ) along with all the contents/photos for the flyer.
Width - 210 mm
Height - 297 mm
Please also see attached the previous flyer which we feel is in need of an upgrade !
Flyer will also be used on social media pages.
Creating next level athletes !
Providing a platform and the correct environment for young football players to develop and fulfil their potential.
Why choose KTR Football Academy
- Multiple programs for everyone
- WAPL qualified & experienced coaches
- Safe and fun environment
- All coaches police checked
- Coaches Emergency First Aid Qualified
- Coaches Safeguarding Children Qualified
- Develop new skills
- Make new friends
- Improve your fitness
REGISTER NOW!
www.brightfieldathletix.example
+968 912 40637
Picturegram/Linkbook - ktrfootballacademy

```html
<!DOCTYPE html>
<html lang="en">
<head>
<meta charset="utf-8">
<title>KTR Football Academy Flyer</title>
<link href="https://fonts.googleapis.com/css2?family=Anton&family=Montserrat:wght@500;600;700&family=Roboto+Condensed:wght@700;800&display=swap" rel="stylesheet">
<style>
  :root{
    --green:#7dc242;
    --green-dark:#2e7d32;
    --grey:#5d5e60;
    --grey-dark:#4a4b4d;
    --white:#ffffff;
    --backdrop:#e4e5ea;
  }
  *{margin:0;padding:0;box-sizing:border-box}
  html,body{width:1200px;height:856px;overflow:hidden;background:var(--backdrop)}
  .stage{position:relative;width:1200px;height:856px}
  .flyer{position:absolute;left:297px;top:0;width:605px;height:856px;background:var(--white);overflow:hidden;font-family:"Montserrat",sans-serif}
  .frame-lines{position:absolute;left:0;top:0;width:605px;height:856px}
  .crest{position:absolute;left:84px;top:60px;width:142px;height:160px;display:flex;flex-direction:column;align-items:center;justify-content:center;gap:8px}
  .crest-dot{width:22px;height:22px;border-radius:50%;background:var(--green)}
  .crest-name{font-family:"Montserrat",sans-serif;font-weight:700;color:var(--grey);font-size:17px;line-height:1.15;text-align:center}
  .headline{position:absolute;left:244px;top:36px;font-family:"Anton",sans-serif;line-height:1}
  .headline .creating{display:block;color:var(--grey);font-size:64px;letter-spacing:0.5px}
  .headline .next{display:block;color:var(--green);font-size:104px;margin-top:-10px;letter-spacing:-1px}
  .headline .level{display:block;color:var(--grey);font-size:40px;margin-top:-8px}
  .mission-band{position:absolute;left:0;top:246px;width:605px;height:204px;background:var(--grey)}
  .mission{position:absolute;left:16px;top:254px;color:var(--white);font-weight:600;font-size:19.5px;line-height:1.05}
  .mission .accent{color:var(--green);font-weight:700;font-size:24px}
  .pitch-photo{position:absolute;left:0;top:450px;width:605px;height:352px;background:linear-gradient(180deg,#dfe5e2 0%,#cfdcd3 55%,#b9cfbd 100%)}
  .players-photo{position:absolute;left:252px;top:250px;width:305px;height:540px;border-radius:40px 40px 8px 8px;background:linear-gradient(180deg,#8fa88f 0%,#2f7a3c 35%,#2a6f37 70%,#c9cfc9 100%);opacity:.92}
  .why{position:absolute;left:15px;top:582px}
  .why-title{font-weight:700;font-size:16px;line-height:1.2;color:var(--grey)}
  .why-title .accent{color:var(--green)}
  .reasons{list-style:none;margin-top:6px}
  .reasons li{display:flex;align-items:center;gap:8px;font-size:10.4px;font-weight:500;color:var(--grey-dark);height:18.4px}
  .reasons li::before{content:"";width:10px;height:11px;background:var(--grey);border-radius:2px}
  .footer-band{position:absolute;left:0;top:802px;width:605px;height:54px;background:var(--grey)}
  .register{position:absolute;left:19px;top:806px;font-family:"Roboto Condensed",sans-serif;font-weight:800;font-size:11px;color:var(--white)}
  .contact-bar{position:absolute;left:0;top:823px;width:490px;height:27px;background:var(--green);clip-path:polygon(0 0,100% 0,97% 100%,0 100%);display:flex;align-items:center;padding-left:19px;gap:18px;font-family:"Roboto Condensed",sans-serif;font-weight:800;font-size:16px;color:var(--white)}
  .contact-item{display:flex;align-items:center;gap:5px}
  .contact-item svg{width:14px;height:14px}
  .contact-item .web{font-size:15px}
  .socials{position:absolute;left:500px;top:820px;display:flex;flex-direction:column;gap:3px;font-family:"Montserrat",sans-serif;font-weight:700;font-size:10px;color:var(--white)}
  .socials span{display:flex;align-items:center;gap:4px}
  .socials span::before{content:"";width:8px;height:8px;border-radius:50%;background:var(--white)}
</style>
</head>
<body>
<div class="stage">
  <article class="flyer">
    <div class="pitch-photo" role="img" aria-label="Faded background photo of young players in a football match on a pitch"></div>

    <svg class="frame-lines" viewBox="0 0 605 856" aria-hidden="true">
      <path d="M54 0 V470 Q54 505 90 530 L330 700" fill="none" stroke="#7dc242" stroke-width="13"/>
      <path d="M553 0 V470 Q553 505 517 530 L360 650" fill="none" stroke="#7dc242" stroke-width="13"/>
      <path d="M78 29 H526 V246" fill="none" stroke="#5d5e60" stroke-width="2"/>
      <path d="M78 29 V246" fill="none" stroke="#5d5e60" stroke-width="2"/>
      <path d="M78 450 V470 Q80 500 120 525 L330 690" fill="none" stroke="#4a4b4d" stroke-width="1.5"/>
    </svg>

    <div class="crest">
      <span class="crest-dot"></span>
      <span class="crest-name">KTR<br>Football<br>Academy</span>
    </div>

    <h1 class="headline">
      <span class="creating">Creating</span>
      <span class="next">NEXT</span>
      <span class="level">level athletes</span>
    </h1>

    <div class="mission-band"></div>
    <p class="mission">
      Providing a <span class="accent">Platform</span><br>
      and the correct<br>
      <span class="accent">Environment</span><br>
      for young football<br>
      <span class="accent">Players</span><br>
      to develop and fulfil<br>
      their <span class="accent">Potential</span>
    </p>

    <div class="players-photo" role="img" aria-label="Photo of two young academy players in green kit, each with one foot on a football"></div>

    <section class="why">
      <h2 class="why-title"><span class="accent">Why choose</span> KTR<br>Football Academy</h2>
      <ul class="reasons">
        <li>Multiple programs for everyone</li>
        <li>WAPL qualified &amp; experienced coaches</li>
        <li>Safe and fun environment</li>
        <li>All coaches police checked</li>
        <li>Coaches Emergency First Aid Qualified</li>
        <li>Coaches Safeguarding Children Qualified</li>
        <li>Develop new skills</li>
        <li>Make new friends</li>
        <li>Improve your fitness</li>
      </ul>
    </section>

    <div class="footer-band"></div>
    <p class="register">REGISTER NOW!</p>
    <div class="contact-bar">
      <span class="contact-item">
        <svg viewBox="0 0 16 16" fill="none" stroke="#4a4b4d" stroke-width="1.4"><circle cx="8" cy="8" r="6.5"/><ellipse cx="8" cy="8" rx="3" ry="6.5"/><path d="M1.5 8h13M2.5 4.8h11M2.5 11.2h11"/></svg>
        <span class="web">www.brightfieldathletix.example</span>
      </span>
      <span class="contact-item">
        <svg viewBox="0 0 16 16" fill="none" stroke="#4a4b4d" stroke-width="1.4"><path d="M4 2l2.5 3-1.5 1.5c.8 1.8 2.2 3.2 4 4L10.5 9 13.5 11.5 12 14C7 13.5 2.5 9 2 4z"/></svg>
        +968 912 40637
      </span>
    </div>
    <div class="socials">
      <span>Linkbook</span>
      <span>Picturegram</span>
    </div>
  </article>
</div>
</body>
</html>
```